Broschüre im Bereich Steuerberatung
Zielgruppe
Steuerberatung
Aufgabenstellung
Die Seite 1 wäre eigentlich fertig, natürlich bin ich offen für Optimierungen. Die weiteren fünf Seiten gilt es noch zu gestalten:
Seite 1
Buchhaltung
Lohnwesen
Steuern
Firmengründung
Kontakt

```html
<!DOCTYPE html>
<html lang="de">
<head>
<meta charset="utf-8">
<title>Broschüre Treuhand</title>
<link href="https://fonts.googleapis.com/css2?family=Jost:wght@400;500;600;700&family=Oswald:wght@400&family=Source+Serif+4:wght@300;400&display=swap" rel="stylesheet">
<style>
:root{
  --stage:#dcdcd5;
  --paper:#ffffff;
  --navy:#1b3a7a;
  --orange:#e85d13;
  --ink:#222222;
}
*{margin:0;padding:0;box-sizing:border-box}
html,body{width:1200px;height:883px;overflow:hidden;background:var(--stage)}
body{position:relative;font-family:"Jost",sans-serif;color:var(--ink)}
.page{position:absolute;width:505px;height:357px;background:var(--paper)}
.p1{left:65px;top:63px}.p2{left:618px;top:63px}
.p3{left:65px;top:454px}.p4{left:618px;top:454px}

.claim{position:absolute;left:21px;top:42px;font-family:"Oswald",sans-serif;font-size:12.5px;letter-spacing:3.2px;color:var(--navy);display:flex;align-items:center;white-space:nowrap}
.claim .dot{display:inline-block;width:5px;height:5px;border-radius:50%;background:var(--orange);margin:0 4px 0 1px}

.photo{position:absolute;left:21px;top:72px;width:240px;height:240px;overflow:hidden}
.photo.street{background:linear-gradient(160deg,#8a6a8a 0%,#6b7a8a 35%,#4e6e4e 60%,#7a6a70 100%)}
.photo.green{background:linear-gradient(120deg,#e08a4a 0%,#9aa050 35%,#4f7e5a 60%,#3d76a8 100%)}
.photo.glass{background:linear-gradient(110deg,#b9a43a 0%,#7f9a48 30%,#3e6fa0 65%,#2d5a96 100%)}
.photo.avenue{background:linear-gradient(150deg,#c27a48 0%,#8c6f7a 40%,#4f6a52 70%,#8a7288 100%)}
.bigword{position:absolute;right:10px;font-family:"Source Serif 4",serif;font-weight:300;color:#fff;line-height:.85;text-align:right}

.brandword{top:16px;font-size:48px}
.brandsub{position:absolute;left:140px;top:60px;font-size:7.5px;letter-spacing:2.6px;color:#f1e4dc;line-height:1.5}
.brandurl{position:absolute;right:22px;bottom:13px;font-size:9px;font-weight:600;color:var(--orange)}

.portrait{position:absolute;left:386px;top:97px;width:100px;height:71px;background:linear-gradient(90deg,#e4e6e8,#d6d9dc)}

.head{position:absolute;left:273px;top:70px;width:220px;font-weight:700;font-size:8px;line-height:1.3;color:var(--navy)}
.sub{position:absolute;left:273px;top:96px;width:225px;font-weight:600;font-size:6px;line-height:1.3;color:var(--orange)}
.txt{position:absolute;font-size:4.8px;line-height:1.5;color:var(--ink);text-align:justify}
.txt p+p{margin-top:5px}
.sv h3{font-size:7.5px;font-weight:600;color:var(--navy);letter-spacing:.2px;margin-bottom:2px}

.calc{position:absolute;width:64px;height:64px;border-radius:50%;background:var(--orange);border:2px solid #fff;box-shadow:0 0 0 1px var(--orange)}
.calc svg{position:absolute;left:16px;top:16px}
.calclink{position:absolute;font-size:6px;font-weight:600;line-height:1.35;color:var(--orange)}

.point{position:absolute;left:386px;width:97px;font-size:5.4px;font-weight:600;line-height:1.35;color:var(--navy);padding-left:16px;text-align:justify}
.point .arr{position:absolute;left:0;top:-2px;width:11px;height:11px;border-radius:50%;background:var(--orange)}

.steps{position:absolute;left:440px;top:118px;width:50px;text-align:center}
.step{height:45px;font-size:5.2px;font-weight:600;line-height:1.3;color:var(--navy)}
.step svg{display:block;margin:0 auto 2px}
.h4{font-size:7.5px;font-weight:600;color:var(--navy);letter-spacing:.3px;margin:6px 0 2px}
</style>
</head>
<body>

<!-- Seite 1: Übersicht -->
<section class="page p1">
  <div class="claim">STEUERN<span class="dot"></span>MEHRWERT<span class="dot"></span>TREUHAND<span class="dot"></span></div>
  <div class="photo street" role="img" aria-label="Stadtstrasse mit Hochhäusern und Bäumen">
    <div class="bigword brandword">corvin</div>
    <div class="brandsub">TREUHAND<br>CONSULTING</div>
    <div class="brandurl">corvintreuhand.ch</div>
  </div>
  <div class="head">Zuverlässig und partnerschaftlich:<br>Ihre massgeschneiderten Treuhand-Lösungen</div>
  <div class="txt" style="left:273px;top:97px;width:96px">
    <p>Sie möchten Ihre Steuern, Ihre Buchhaltung oder Ihr Lohnwesen in verlässliche Hände geben? Sie legen Wert auf eine persönliche Betreuung mit gleichbleibendem Ansprechpartner, auf individuelle Strategien und auf ein angenehmes Miteinander?</p>
    <p>Dann freue ich mich auf Ihre Kontaktaufnahme.</p>
  </div>
  <div class="portrait" role="img" aria-label="Porträtfoto der Inhaberin"></div>
  <div class="txt sv" style="left:273px;top:192px;width:96px">
    <h3>BUCHHALTUNG</h3>
    <p>Buchhaltung ist komplex und aufwendig – das kostet Unternehmer viel Zeit, die sie anderswo wertschöpfend einsetzen könnten. Mithilfe moderner Hilfsmittel und bewährter Prozesse entlaste ich Sie zuverlässig und zum Fixpreis.</p>
  </div>
  <div class="txt sv" style="left:386px;top:192px;width:96px">
    <h3>STEUERERKLÄRUNG</h3>
    <p>Jeder möchte seine Steuerlast optimieren, nur wenige setzen sich aktiv damit auseinander. Denn das kostet Zeit und verlangt nach umfangreichem Wissen. Vertrauen Sie mir Ihre Steuererklärungen an – und holen Sie sich zurück, was Ihnen zusteht.</p>
  </div>
  <div class="txt sv" style="left:273px;top:259px;width:96px">
    <h3>LOHNWESEN</h3>
    <p>Entscheiden Sie selbst, in welcher Form Sie auf meine Expertise zugreifen, um sich beim Thema Lohnbuchhaltung zu entlasten.</p>
  </div>
  <div class="txt sv" style="left:386px;top:259px;width:96px">
    <h3>FIRMENGRÜNDUNG</h3>
    <p>Gründen Sie Ihre Schweizer Gesellschaft schnell und sicher. Mit meiner langjährigen Erfahrung, meinem Wissen und meiner Zusammenarbeit mit einem versierten Notar unterstütze ich Sie zuverlässig – auch über Ihre Gründung hinaus.</p>
  </div>
</section>

<!-- Seite 2: Buchhaltung -->
<section class="page p2">
  <div class="claim">ADDITION<span class="dot"></span>SUBTRAKTION<span class="dot"></span>ERFOLG<span class="dot"></span></div>
  <div class="photo green" role="img" aria-label="Baumkronen vor einem gläsernen Hochhaus">
    <div class="bigword" style="top:16px;font-size:50px">buch-<br>haltung</div>
  </div>
  <div class="head" style="left:274px">Buchhaltung kostet Sie viel Zeit<br>– Ich gebe Sie Ihnen zurück</div>
  <div class="sub" style="left:274px">Ich übernehme Ihre Buchhaltung –<br>akribisch, verlässlich, verantwortungsvoll</div>
  <div class="txt" style="left:274px;top:124px;width:96px">
    <p>Unternehmer zählen die Buchhaltung in der Regel nicht zu ihren Leidenschaften.</p>
    <p>Und dennoch ist eine ordentliche Buchhaltung das Rückgrat eines jeden erfolgreichen Betriebs. Es ergibt also durchaus Sinn, hierfür ausreichend Ressourcen bereitzustellen – jedoch nicht die eigenen.</p>
    <p>Wenn Sie selbst oder Ihre Mitarbeiter sich um dieses komplexe „Pflichtthema“ kümmern, bleiben andere, wertschöpfende Tätigkeiten auf der Strecke: neue Kunden akquirieren, Produkte weiterentwickeln, Services ausbauen usw.</p>
  </div>
  <div class="txt" style="left:387px;top:124px;width:96px">
    <p>Die Folge: Es kommt zu unnötigem Mehraufwand und die Entwicklung Ihres Unternehmens schreitet langsamer voran als geplant.</p>
    <p>Beides ist unschön – und beides lässt sich leicht vermeiden. Nutzen Sie Ihre wertvolle Zeit lieber gewinnbringend und überlassen Sie Ihre Buchhaltung einem Profi.</p>
    <p>Mit viel Erfahrung, Wissen und Leidenschaft kümmere ich mich um Ihre Geschäftsvorfälle, während Ihr Team und Sie sich auf Ihre Kerntätigkeit fokussieren.</p>
  </div>
  <div class="calc" style="left:230px;top:256px">
    <svg width="32" height="32" viewBox="0 0 32 32" fill="none" stroke="#fff" stroke-width="2.4" stroke-linecap="round"><rect x="1.5" y="1.5" width="29" height="29" rx="4"/><path d="M7 10h6M19 7l5 5M24 7l-5 5M10 19v6M7 22h6M19 20h6M19 24h6"/></svg>
  </div>
  <div class="calclink" style="left:305px;top:282px">Mit individuellem Preisrechner auf:<br>www.corvintreuhand.ch/treuhand/buchhaltung</div>
</section>

<!-- Seite 3: Lohnwesen -->
<section class="page p3">
  <div class="claim">BERECHNUNG<span class="dot"></span>PRÄZISION<span class="dot"></span>ENTLASTUNG<span class="dot"></span></div>
  <div class="photo glass" role="img" aria-label="Glasfassade eines Bürogebäudes mit Bäumen">
    <div class="bigword" style="top:16px;font-size:50px">lohn</div>
  </div>
  <div class="head">Lohnbuchhaltung ohne Stress:<br>So gewinnen Sie mehr Zeit</div>
  <div class="sub">Ich erledige Ihr Lohnwesen – präzise, sicher, zuverlässig</div>
  <div class="txt" style="left:273px;top:122px;width:96px">
    <p>Sicherlich stimmen Sie mir zu, wenn ich das Personalwesen und die Salärad­ministration zu den sensiblen Bereichen Ihres Unternehmens zähle. Schliesslich erwarten Ihre Mitarbeiter, dass ihre Gehälter pünktlich auf dem Konto eingehen.</p>
    <p>Doch die Lohnbuchhaltung ist komplex und daher zeitaufwändig – sie bindet wertvolle Ressourcen, die Ihnen für andere, wert schöpfende Tätigkeiten fehlen.</p>
    <p>Holen Sie sich die Zeit zurück und legen Sie Ihre Lohnbuchhaltung in meine Hände. Dabei haben Sie die Wahl zwischen Optimierung und Outsourcing:</p>
  </div>
  <div class="point" style="top:122px"><span class="arr"><svg width="11" height="11" viewBox="0 0 11 11" fill="none" stroke="#fff" stroke-width="1.2" stroke-linecap="round"><path d="M3 5.5h5M6 3.5l2 2-2 2"/></svg></span>Sie übernehmen die vorbereitenden Arbeiten, während ich mich um die Umsetzung kümmere. So optimieren wir gemeinsam Ihre Vorgänge und entlasten Ihre interne Buchhaltung.</div>
  <div class="point" style="top:180px"><span class="arr"><svg width="11" height="11" viewBox="0 0 11 11" fill="none" stroke="#fff" stroke-width="1.2" stroke-linecap="round"><path d="M3 5.5h5M6 3.5l2 2-2 2"/></svg></span>Sie lagern Ihre Lohnbuchhaltung an mich aus. Insbesondere kleine und mittlere Unternehmen profitieren vom Outsourcing immens, da sie sich von diesem Thema komplett befreien.</div>
</section>

<!-- Seite 4: Steuern -->
<section class="page p4">
  <div class="claim">EFFIZIENZ<span class="dot"></span>SICHERHEIT<span class="dot"></span>GENAU<span class="dot"></span></div>
  <div class="photo avenue" role="img" aria-label="Baumgesäumte Allee zwischen Bürohäusern">
    <div class="bigword" style="top:16px;font-size:50px">steuern</div>
  </div>
  <div class="head" style="left:274px">Professionell und transparent:<br>Ihre Steuererklärung und Steuerberatung</div>
  <div class="sub" style="left:274px">Ich kümmere mich persönlich um Ihre Steuerangelegenheiten</div>
  <div class="txt" style="left:274px;top:118px;width:137px">
    <p>Steuern sind ein sensibles Thema – schliesslich geht es um Ihr Geld. Setzen Sie gleich auf professionelle Unterstützung: Vermeiden Sie teure Fehler, sparen Sie viel Zeit und schonen Sie Ihre Nerven.</p>
    <div class="h4">FÜR PRIVATPERSONEN</div>
    <p>Weshalb ich mir viel Zeit für Sie nehme und Sie individuell betreue? Weil wir mit Konzepten „von der Stange“ bei Ihrer Steuererklärung nicht weit kommen.</p>
    <p>Hingegen habe ich die Abläufe rund um Ihre Steuerberatung standardisiert – um es Ihnen einfach zu machen: Wir tauschen uns per E-Mail, Telefon, Videocall oder per Post aus. So erhalten Sie schnelle Ergebnisse und sparen sich Weg und Kosten für einen persönlichen Termin.</p>
  </div>
  <div class="steps">
    <div class="step"><svg width="16" height="20" viewBox="0 0 16 20" fill="none" stroke="var(--orange)" stroke-width="1.2"><rect x="1" y="1" width="14" height="18" rx="1"/><circle cx="8" cy="10" r="4"/><path d="M6 10l1.5 1.5L10.5 8.5"/></svg>Checkliste<br>ausfüllen</div>
    <div class="step"><svg width="20" height="20" viewBox="0 0 20 20" fill="none" stroke="var(--orange)" stroke-width="1.2"><rect x="5" y="1" width="11" height="12"/><path d="M8 5h5M8 8h5M2 15c3-2 6-1 8 0h6M2 18h14"/></svg>Unterlagen<br>bereitstellen</div>
    <div class="step"><svg width="22" height="16" viewBox="0 0 22 16" fill="none" stroke="var(--orange)" stroke-width="1.2"><rect x="1" y="2" width="20" height="13"/><path d="M1 2l10 8 10-8M1 15l7-6M21 15l-7-6"/></svg>Unterlagen<br>übergeben</div>
    <div class="step"><svg width="16" height="20" viewBox="0 0 16 20" fill="none" stroke="var(--orange)" stroke-width="1.2"><rect x="1" y="1" width="14" height="18"/><rect x="4" y="5" width="8" height="10"/><path d="M5 13l6-6"/><circle cx="6" cy="8" r=".8"/><circle cx="10" cy="12" r=".8"/></svg>Meine<br>Arbeit</div>
    <div class="step"><svg width="16" height="20" viewBox="0 0 16 20" fill="none" stroke="var(--orange)" stroke-width="1.2"><path d="M1 1h9l5 5v13H1z M10 1v5h5"/><path d="M8 16V9M5 12l3-3 3 3"/></svg>Unterschreiben<br>+ Abgeben</div>
  </div>
  <div class="calc" style="left:230px;top:234px">
    <svg width="32" height="32" viewBox="0 0 32 32" fill="none" stroke="#fff" stroke-width="2.4" stroke-linecap="round"><rect x="1.5" y="1.5" width="29" height="29" rx="4"/><path d="M7 10h6M19 7l5 5M24 7l-5 5M10 19v6M7 22h6M19 20h6M19 24h6"/></svg>
  </div>
  <div class="calclink" style="left:303px;top:262px">Mit individuellem Preisrechner auf:<br>www.corvintreuhand.ch</div>
</section>

</body>
</html>
```